User Interface Designer Needed

I need a few designs for a property law comparison website. We assist the public with finding a solicitor for the purchase or sale of their house and units. We are currently in the process of creating a questionnaire based woo commerce product filter using gravity forms. I'd like to see designs that use the logo colours. Users will be selecting options such as "Buying" or "Selling", they will then be selecting options such as "House" "Unit" or "Land". Details attached. The final design should communicate ease and simplicity. Questions will be answered one at a time, and the next question is dependent on the answer to the question prior

Target Market(s)

First home buyers, people from ages 18-80 make and female looking to get rid of the hassle of ringing around and going from website to website trying to get a quote

Industry/Entity Type

Real Estate

Number of Pages Required

1 page

Colors
33a6d7

Requirements
Must have
• A design for every question
Nice to have
• Simple symbols or simplistic pictures incorporated, even better if you can turn the question into a picture instead of words eg. A picture of a house, a picture of a unit and a picture of land instead of written answers

```html
<!DOCTYPE html>
<html lang="en">
<head>
<meta charset="utf-8">
<title>Homequote – Buyer</title>
<link href="https://fonts.googleapis.com/css2?family=Open+Sans:wght@300;400;600;700&display=swap" rel="stylesheet">
<style>
:root{
  --brand:#1d8fc0;
  --brand-dim:#1a7fab;
  --modal:#00aeef;
  --ink:#1b1b1b;
  --bar:#141414;
  --panel:#eeeeee;
  --card:#efefef;
  --muted:#6f6f6f;
  --side:#dcdcdc;
  --footer:#0d4c66;
  --white:#ffffff;
}
*{box-sizing:border-box;margin:0;padding:0}
html,body{width:1200px;height:1062px;overflow:hidden}
body{position:relative;font-family:"Open Sans",Arial,sans-serif;background:#2c2c2c;color:var(--ink)}
.abs{position:absolute}

.brand-area{left:0;top:0;width:265px;height:118px;background:#e9e9e9;display:flex;align-items:center;padding-left:10px;gap:8px}
.brand-dot{width:36px;height:36px;border-radius:50%;background:var(--brand)}
.brand-name{font-size:27px;font-weight:600;color:var(--brand);letter-spacing:-0.5px}

.topbar{left:265px;top:0;width:935px;height:64px;background:var(--bar)}
.topnav{position:absolute;right:16px;top:22px;display:flex;gap:38px;font-size:14px;color:#9a9a9a}
.topnav span{display:flex;align-items:center;gap:7px}
.topnav svg{width:13px;height:13px;fill:#9a9a9a}

.subbar{left:265px;top:64px;width:935px;height:54px;background:var(--panel)}
.subbar h1{position:absolute;left:0;right:0;top:14px;text-align:center;font-size:21px;font-weight:600;color:var(--brand)}
.help{position:absolute;right:16px;top:17px;width:20px;height:20px;border-radius:50%;background:var(--brand);color:var(--white);font-size:14px;font-weight:700;text-align:center;line-height:20px}

.sidebar{left:0;top:118px;width:270px;height:896px;background:var(--side)}
.role-head{height:66px;background:var(--brand);display:flex;align-items:center;justify-content:space-between;padding:0 24px 0 34px;color:#7fd0f0;font-size:28px;font-weight:400}
.role-head svg{width:22px;height:14px}
.role{height:62px;border-bottom:1px solid #c8c8c8;display:flex;align-items:center;gap:14px;padding-left:32px;font-size:15.5px;color:#3a3a3a}
.role svg{width:19px;height:17px;fill:#555}
.role.active{background:#f4f4f4;width:275px;color:var(--brand);border-left:3px solid var(--brand);padding-left:29px}
.role.active svg{fill:var(--brand)}

.scene{left:270px;top:118px;width:930px;height:896px;background:linear-gradient(120deg,#3a3a3a 0%,#4d4843 45%,#6d6158 70%,#534a44 100%)}

.card{position:absolute;width:276px;height:364px;background:var(--card)}
.step{position:absolute;left:12px;top:24px;font-size:15px;font-weight:600;color:#555;display:flex;align-items:center;gap:8px}
.step b{width:21px;height:21px;border-radius:50%;background:var(--ink);color:var(--white);font-size:10px;font-weight:400;text-align:center;line-height:21px}
.q{position:absolute;left:12px;top:58px;font-size:24px;color:#333}
.opts{position:absolute;left:12px;top:122px;width:251px}
.opt{font-size:13px;color:#555;padding:0 20px;height:32px;display:flex;align-items:center;text-transform:uppercase}
.opt.sel{background:var(--brand-dim);color:#cfe9f5;justify-content:space-between;padding-right:12px}
.opt.tall{height:52px;line-height:17px}
.opt.plain{height:80px;align-items:center;line-height:17px}
.btn{position:absolute;right:12px;top:316px;width:114px;height:32px;background:var(--ink);color:#cfcfcf;font-size:16px;display:flex;align-items:center;justify-content:center;gap:18px}
.btn svg{width:14px;height:14px}
.btn.submit{background:var(--brand-dim);color:#cfe9f5}

.modal{left:529px;top:303px;width:392px;height:369px;background:var(--modal);color:var(--white)}
.modal h2{position:absolute;left:51px;top:58px;font-size:18px;font-weight:700;letter-spacing:0.8px}
.close{position:absolute;left:357px;top:19px;width:20px;height:20px}
.modal ul{list-style:none;position:absolute;left:55px;top:130px}
.modal li{height:48px;font-size:15.5px;display:flex;align-items:center;gap:28px}
.modal li::before{content:"";width:9px;height:9px;border-radius:50%;background:var(--white)}

.footer{left:0;top:1014px;width:1200px;height:48px;background:var(--footer);color:#7aa4b6;font-size:11.5px}
.footer p{position:absolute;left:58px;top:17px}
.social{position:absolute;right:16px;top:14px;display:flex;gap:8px}
.social i{width:20px;height:20px;background:#6c95a7;display:block}
</style>
</head>
<body>

<div class="abs brand-area"><span class="brand-dot"></span><span class="brand-name">Homequote.com.au</span></div>

<header class="abs topbar">
  <nav class="topnav">
    <span><svg viewBox="0 0 16 16"><path d="M8 1 0 8h2v7h4v-5h4v5h4V8h2z"/></svg>Home</span>
    <span><svg viewBox="0 0 16 16"><path d="M1 3h6v6H4v4H1zM9 3h6v6h-3v4H9z"/></svg>Quotes</span>
    <span><svg viewBox="0 0 16 16"><circle cx="8" cy="5" r="4"/><path d="M1 16c0-5 3-6 7-6s7 1 7 6z"/></svg>About</span>
  </nav>
</header>

<div class="abs subbar"><h1>Buyer</h1><span class="help">?</span></div>

<aside class="abs sidebar">
  <div class="role-head">I am a<svg viewBox="0 0 22 14"><path d="M2 2l9 9 9-9" fill="none" stroke="#7fd0f0" stroke-width="3"/></svg></div>
  <div class="role active"><svg viewBox="0 0 20 17"><path d="M0 5h20l-2 12H2zM5 5l4-5M15 5l-4-5" /></svg>BUYER</div>
  <div class="role"><svg viewBox="0 0 20 17"><rect x="3" y="0" width="14" height="9"/><rect x="0" y="11" width="20" height="6"/></svg>SELLER</div>
  <div class="role"><svg viewBox="0 0 20 17"><path d="M0 3h20v11H0z" fill="none" stroke="#555" stroke-width="2"/><circle cx="10" cy="8.5" r="3"/></svg>BUYER AND SELLER</div>
</aside>

<main class="abs scene" role="img" aria-label="Photo of a hand opening a front door, darkened behind the questionnaire">

  <section class="card" style="left:32px;top:49px">
    <div class="step">Step <b>1</b></div>
    <div class="q">I’m buying a</div>
    <div class="opts">
      <div class="opt sel">House</div>
      <div class="opt">Unit</div>
      <div class="opt">Land</div>
      <div class="opt">House and land packages</div>
    </div>
    <div class="btn">NEXT<svg viewBox="0 0 14 14"><circle cx="7" cy="7" r="6" fill="none" stroke="#cfcfcf"/><path d="M4 7h6M7 4l3 3-3 3" fill="none" stroke="#cfcfcf"/></svg></div>
  </section>

  <section class="card" style="left:334px;top:49px">
    <div class="step">Step <b>2</b></div>
    <div class="q">I would like</div>
    <div class="opts"><div class="opt sel">Only the searches I need</div></div>
  </section>

  <section class="card" style="left:635px;top:49px">
    <div class="step">Step <b>3</b></div>
    <div class="opts">
      <div class="opt sel tall"><span>I want my quote to include<br>unlimited extensions</span><span>›</span></div>
      <div class="opt plain">I only want to pay<br>for extensions if I need them</div>
    </div>
    <div class="btn">NEXT<svg viewBox="0 0 14 14"><circle cx="7" cy="7" r="6" fill="none" stroke="#cfcfcf"/><path d="M4 7h6M7 4l3 3-3 3" fill="none" stroke="#cfcfcf"/></svg></div>
  </section>

  <section class="card" style="left:34px;top:442px">
    <div class="step">Step <b>4</b></div>
    <div class="opts">
      <div class="opt sel"><span>I have signed a contract</span><span>›</span></div>
      <div class="opt plain">I haven’t signed a allow for<br>the possibility of contract yet</div>
    </div>
    <div class="btn">NEXT<svg viewBox="0 0 14 14"><circle cx="7" cy="7" r="6" fill="none" stroke="#cfcfcf"/><path d="M4 7h6M7 4l3 3-3 3" fill="none" stroke="#cfcfcf"/></svg></div>
  </section>

  <section class="card" style="left:337px;top:442px">
    <div class="opts">
      <div class="opt sel tall"><span>I want my quote to<br>allow for the possibility of</span><span>›</span></div>
      <div class="opt plain" style="line-height:20px">Terminations<br>Deed of recissions<br>Deed of variations</div>
    </div>
    <div class="btn submit">SUBMIT</div>
  </section>
</main>

<div class="abs modal" role="dialog" aria-label="Only the searches I need">
  <svg class="close" viewBox="0 0 20 20"><path d="M4 4l12 12M16 4 4 16" stroke="#fff" stroke-width="3.5"/></svg>
  <h2>ONLY THE SEARCHES I NEED</h2>
  <ul>
    <li>Title Search x 2</li>
    <li>Council Rates Search</li>
    <li>Special Water Metre Read</li>
    <li>Land Tax Clearance Certificate</li>
  </ul>
</div>

<footer class="abs footer">
  <p>© 2012-2016 YOURSITE | ALL RIGHTS RESERVED | PRIVACY POLICY | TERMS</p>
  <div class="social"><i></i><i></i><i></i><i></i></div>
</footer>

</body>
</html>
```